Business card design for a dynamic IT consulting company

We need a business card design for a young firm, specialized in the Telecommunications/Consulting industry. The name of the company is Brask and Partners Business Consulting Ltd. (Short name: Brask and Partnes)
Brask = solve read reverse, so we aim to be uncomplicated and solution-oriented. The small pipe in our logo is also related to the word solve. So we need a new business card design, which is simple, eye catching and something non traditional (I would probably prefer a square shaped design rather than a rectangle, but open for suggestions). Attached our logo.

Target Market(s)

Usually our customers are Tier1 Telecoms providers (Q-Linkra, Parnexo, etc) and their executives.

Industry/Entity Type

Business

Contact Information for Business Card

Name: Gergely Halmindo
Email: g.halmindo@braskpartnera.hu
Web: www.braskpartnera.hu
Mobile: +36 30 555 0192
Title: Managing Director

Optional:
Company name: Brask and Partners Ltd.
Address: 1047 Budapest, Ravaszi str. 17/B, Hungary

Font styles to use
Other font styles liked:
• helveticaneue_medium, Prime Regular are used now.

Colors

Designer to choose colors to be used in the design.

Requirements
Must have
• I would like to have a 2 sided design.
Nice to have
• I thought if we make the logo a bit bigger (without the company name), that could go to the back with the company name below. I though, if the pipe in the logo is somehow touchable on the business card, would be nice and unique.

```html
<!DOCTYPE html>
<html lang="en">
<head>
<meta charset="utf-8">
<title>Brask &amp; Partners – Business Card</title>
<link rel="stylesheet" href="https://fonts.googleapis.com/css2?family=Exo+2:wght@400&family=Open+Sans:wght@600;700&display=swap">
<style>
  :root {
    --backdrop: #3a3a3c;
    --card-dark: #2b303b;
    --card-light: #f6f6f5;
    --ink-light: #ffffff;
    --ink-grey: #555a60;
    --ink-dark: #2e3035;
    --accent-cyan: #22a8d8;
    --tint-cyan: rgba(120, 200, 235, 0.45);
    --tint-magenta: rgba(215, 140, 190, 0.40);
    --tint-dark-cyan: rgba(40, 120, 160, 0.55);
    --tint-dark-magenta: rgba(130, 50, 100, 0.55);
  }
  * { margin: 0; padding: 0; box-sizing: border-box; }
  html, body { width: 1200px; height: 801px; overflow: hidden; }
  body { background: var(--backdrop); position: relative; font-family: "Open Sans", Arial, sans-serif; }

  .card {
    position: absolute;
    top: 251px;
    height: 274px;
    border-radius: 14px;
    overflow: hidden;
  }
  .card--back { left: 117px; width: 475px; background: var(--card-dark); }
  .card--front { left: 611px; width: 478px; background: var(--card-light); }

  .decor { position: absolute; }
  .card--back .decor--top {
    left: 0; top: 0; width: 130px; height: 102px;
    background: linear-gradient(135deg, var(--tint-dark-magenta), var(--tint-dark-cyan) 70%, transparent);
    opacity: .6;
  }
  .card--back .decor--bottom {
    right: 0; bottom: 0; width: 134px; height: 100px;
    background: linear-gradient(315deg, var(--tint-dark-magenta), var(--tint-dark-cyan) 70%, transparent);
    opacity: .6;
  }
  .card--front .decor--top {
    left: 0; top: 0; width: 140px; height: 104px;
    background: linear-gradient(160deg, var(--tint-magenta), var(--tint-cyan) 60%, transparent);
    opacity: .55;
  }
  .card--front .decor--bottom {
    left: 0; bottom: 0; width: 140px; height: 100px;
    background: linear-gradient(20deg, var(--tint-magenta), var(--tint-cyan) 60%, transparent);
    opacity: .55;
  }

  .wordmark {
    position: absolute;
    display: flex;
    align-items: center;
    gap: 12px;
  }
  .wordmark__square { width: 14px; height: 14px; background: var(--accent-cyan); }
  .wordmark__name {
    font-family: "Exo 2", Arial, sans-serif;
    font-weight: 400;
    font-size: 32px;
    line-height: 1;
  }
  .card--back .wordmark { left: 64px; top: 122px; }
  .card--back .wordmark__name { color: var(--ink-light); }
  .card--front .wordmark { left: 68px; top: 122px; }
  .card--front .wordmark__name { color: var(--ink-grey); }

  .person { position: absolute; right: 51px; top: 40px; text-align: right; }
  .person__name { color: var(--accent-cyan); font-weight: 700; font-size: 12px; letter-spacing: .3px; }
  .person__title { color: var(--ink-dark); font-weight: 700; font-size: 9px; margin-top: 5px; }

  .contacts { position: absolute; right: 40px; top: 182px; list-style: none; }
  .contacts li {
    display: flex; justify-content: flex-end; align-items: center; gap: 8px;
    color: var(--ink-dark); font-weight: 700; font-size: 11.5px; height: 20px;
  }
  .contacts svg { width: 14px; height: 12px; stroke: var(--accent-cyan); fill: none; stroke-width: 1.2; }
</style>
</head>
<body>
  <section class="card card--back" aria-label="Card back">
    <div class="decor decor--top" role="img" aria-label="Soft pattern of cyan and magenta squares"></div>
    <div class="decor decor--bottom" role="img" aria-label="Soft pattern of cyan and magenta squares"></div>
    <div class="wordmark">
      <span class="wordmark__square"></span>
      <span class="wordmark__name">Brask &amp; Partners</span>
    </div>
  </section>

  <section class="card card--front" aria-label="Card front">
    <div class="decor decor--top" role="img" aria-label="Soft pattern of pale cyan and pink squares"></div>
    <div class="decor decor--bottom" role="img" aria-label="Soft pattern of pale cyan and pink squares"></div>
    <div class="person">
      <p class="person__name">GERGELY HALMINDO</p>
      <p class="person__title">MANAGING DIRECTOR</p>
    </div>
    <div class="wordmark">
      <span class="wordmark__square"></span>
      <span class="wordmark__name">Brask &amp; Partners</span>
    </div>
    <ul class="contacts">
      <li>+36 30 555 0192
        <svg viewBox="0 0 14 12"><path d="M1 4 Q7 0 13 4 L11 6 L9 4.5 L5 4.5 L3 6 Z"/><rect x="3" y="6" width="8" height="5" rx="1"/></svg>
      </li>
      <li>g.halmindo@braskpartnera.hu
        <svg viewBox="0 0 14 12"><rect x="1" y="2" width="12" height="8"/><path d="M1 2 L7 7 L13 2"/></svg>
      </li>
      <li>www.braskpartnera.hu
        <svg viewBox="0 0 14 12"><circle cx="7" cy="6" r="5"/><ellipse cx="7" cy="6" rx="2.2" ry="5"/><path d="M2 6 H12"/></svg>
      </li>
    </ul>
  </section>
</body>
</html>
```